TW Groundworks Capability Statement

I need to design a two page Capability statement for our Civil Construction company that looks professional and can be issued to clients in electronic or print form to show our capabilities.

We have an existing Logo and website https://twgroundworks.com.au/

It should include space for the below:
- Company heading/logo plus ABN, ACN and full contact details
- About Us – Mission, vision, values
- Our Service Offering / Core competencies
- Accreditations/certifications

Designs look the same

```html
<!DOCTYPE html>
<html lang="en">
<head>
<meta charset="utf-8">
<title>TW Groundworks – Capability Statement</title>
<link rel="stylesheet" href="https://fonts.googleapis.com/css2?family=Carlito:wght@400;700&family=Saira+Condensed:wght@500;600&display=swap">
<style>
:root{
  --navy:#29296f;
  --yellow:#fbb01a;
  --cream:#fff1d9;
  --ink:#3b3b3b;
  --paper:#ffffff;
  --backdrop:#b3b3b3;
  --head:"Saira Condensed",sans-serif;
  --body:"Carlito","Calibri",sans-serif;
}
*{margin:0;padding:0;box-sizing:border-box}
html,body{width:1200px;height:846px;overflow:hidden;background:var(--backdrop)}
.spread{position:relative;width:1200px;height:846px}
.page{position:absolute;top:76px;width:491px;height:694px;background:var(--paper);overflow:hidden;font-family:var(--body);color:var(--ink)}
.page--front{left:84px}
.page--back{left:616px}
.abs{position:absolute}
.shapes{position:absolute;left:0;top:0}
.brand{position:absolute;display:flex;align-items:center;gap:6px;font-family:var(--head);font-weight:600;color:var(--navy);white-space:nowrap}
.brand__mark{background:var(--yellow);display:block}
.brand--front{left:290px;top:36px;font-size:25px}
.brand--front .brand__mark{width:30px;height:30px}
.brand--back{left:362px;top:618px;font-size:15px}
.brand--back .brand__mark{width:18px;height:18px}
.hero-photo{position:absolute;left:0;top:107px;width:491px;height:272px;background:linear-gradient(120deg,#9aa7b6 0%,#d9dde2 40%,#eef0f2 60%,#b9b3a9 100%)}
.cover-title{position:absolute;left:22px;top:345px;font-family:var(--head);font-weight:500;font-size:17px;letter-spacing:3.4px;color:#fff}
.section-title{font-family:var(--head);font-weight:600;color:var(--navy);letter-spacing:2.8px;font-size:15px;line-height:1}
.about-title{position:absolute;left:55px;top:398px}
.about-icon{position:absolute;left:22px;top:394px}
.copy{font-size:8.5px;line-height:10.25px}
.copy p+p{margin-top:2.4px}
.cream-panel{position:absolute;background:var(--cream)}
.about-left{position:absolute;left:22px;top:433px;width:262px}
.about-right{position:absolute;left:313px;top:438px;width:168px}
.footer{position:absolute;left:0;bottom:0;width:491px;height:28px;display:flex;align-items:center;justify-content:flex-end;padding-right:20px;font-family:var(--head);font-weight:500;font-size:9px;letter-spacing:2.2px;color:#fff}
.footer--navy{background:var(--navy)}
.footer--yellow{background:var(--yellow)}
.heading-row{position:absolute;left:81px;display:flex;align-items:center;gap:8px}
.heading-row .square{width:7px;height:7px;background:var(--navy)}
.sub-title{position:absolute;font-family:var(--head);font-weight:600;color:var(--navy);font-size:9.2px;letter-spacing:1.6px;line-height:1}
.bullets{position:absolute;list-style:none;font-size:8.2px;line-height:9.95px}
.bullets li{position:relative;padding-left:14px}
.bullets li::before{content:"";position:absolute;left:1px;top:3.6px;width:2.6px;height:2.6px;border-radius:50%;background:var(--ink)}
.service-icon{position:absolute}
.reason{position:absolute;left:110px;width:340px}
.reason .sub-title{position:static;font-size:8.6px;margin-bottom:4px}
.reason p{font-size:8.3px;line-height:10.3px}
.reason-icon{position:absolute;left:52px;width:36px;height:36px;border-radius:50%;background:#fff;display:flex;align-items:center;justify-content:center}
.contact-line{position:absolute;left:84px;display:flex;align-items:center;gap:6px;font-size:8.4px}
.contact-line b{font-weight:700}
</style>
</head>
<body>
<div class="spread">

  <!-- Page one -->
  <section class="page page--front">
    <svg class="shapes" width="491" height="694" aria-hidden="true">
      <polygon points="0,0 105,107 0,107" fill="var(--yellow)"/>
    </svg>
    <div class="brand brand--front"><span class="brand__mark"></span>TW Groundworks</div>

    <div class="hero-photo" role="img" aria-label="Photo of site team hands discussing plans over a white hard hat, glasses and a calculator on a desk"></div>

    <svg class="shapes" width="491" height="694" aria-hidden="true">
      <polygon points="0,123 256,379 0,379" fill="var(--navy)"/>
      <polygon points="256,379 491,379 491,423 299,423" fill="var(--yellow)"/>
    </svg>
    <h1 class="cover-title">CAPABILITY STATEMENT</h1>

    <div class="cream-panel" style="left:299px;top:423px;width:192px;height:243px"></div>

    <svg class="about-icon" width="23" height="25" viewBox="0 0 23 25" fill="none" stroke="var(--navy)" stroke-width="1.1" aria-hidden="true">
      <rect x="1" y="4" width="15" height="19" rx="1"/>
      <rect x="3.5" y="1.5" width="15" height="19" rx="1" fill="#fff"/>
      <path d="M6 7h8M6 10h10M6 13h10M6 16h7"/>
      <circle cx="18.5" cy="4.5" r="3.5" fill="#fff"/>
      <path d="M18.5 3.5v3M18.5 2.2v.4"/>
    </svg>
    <h2 class="section-title about-title">ABOUT US</h2>

    <div class="about-left copy">
      <p>Tier 1 engineering and project management capability with nimble privately owned and operated mentality.</p>
      <p>Founded by Daniel Harper and Michael Ross, TW Groundworks is a Utilities business focused on underground utilities.</p>
      <p>Daniel &amp; Michael have over 25 years’ combined experience, with the majority of this time being colleagues at national and international engineering services organisations delivering underground utility works. Evolving their careers from graduates to senior managers over seeing program/project budgets greater $100m. TW Groundworks was established through their shared passions for safety, client satisfaction, field productivity and most importantly a positive workplace.</p>
      <p>TW Groundworks leverage our demonstrated experience and countless relationships within the industry to provide market leading service. Our focus is our clients, and finding ways we can make their lives easier. We create a collaborative environment on all our projects by providing as much transparency and visibility as possible which enables us to work together to find mutually beneficial outcomes for all stakeholders. This approach leads to long standing partnerships, and exceptional results for all parties.</p>
    </div>

    <div class="about-right copy">
      <p>Ensuring Safety is the number one priority isn’t just talk at TW Groundworks. It is an engrained philosophy that we live and breathe every day. We understand and are committed to targeting a generative safety culture. An environment with the appropriate safety guards, task specific systems and processes and most importantly empowered people aligned in creating an industry leading safety culture. We do not accept shortcuts and are unwilling to employ or engage with anyone who is not aligned with this safety vision.</p>
      <p>We are a company that wants to enjoy our days work, and while we all have challenging days we believe we are stronger together. This message helps foster an inclusive and supportive team culture that allows us all to take great satisfaction from our achievements and celebrate them as a team.</p>
    </div>

    <footer class="footer footer--navy">WWW.TWGROUNDWORKS.COM.AU</footer>
  </section>

  <!-- Page two -->
  <section class="page page--back">
    <svg class="shapes" width="491" height="694" aria-hidden="true">
      <polygon points="386,0 491,0 491,107" fill="var(--navy)"/>
      <g stroke="var(--yellow)" stroke-width="1" fill="none">
        <path d="M0 39H66M170 39H449V338M0 338H281"/>
        <path d="M0 589H70M180 589H491"/>
      </g>
      <polygon points="280,338 449,338 449,354 296,354" fill="var(--yellow)"/>
      <polygon points="0,608 38,666 0,666" fill="var(--yellow)"/>
    </svg>

    <div class="heading-row" style="top:31px"><span class="square"></span><h2 class="section-title">SERVICES</h2></div>

    <!-- Water -->
    <svg class="service-icon" style="left:43px;top:61px" width="33" height="34" viewBox="0 0 33 34" fill="none" stroke="var(--navy)" stroke-width="1.2" aria-hidden="true">
      <path d="M2 2v26M31 2v26M2 8q14.5 12 29 0M1 22h31M1 26h31M7 11v11M12 14v8M16.5 15v7M21 14v8M26 11v11"/>
      <rect x="1" y="28" width="31" height="4"/>
    </svg>
    <h3 class="sub-title" style="left:96px;top:53px">WATER INFRASTRUCTURE</h3>
    <ul class="bullets" style="left:96px;top:67px;width:170px">
      <li>Accredited contractor with major Water Authorities</li>
      <li>Constructability design reviews from highly experienced professionals</li>
      <li>Reticulation mains and larger pipelines</li>
      <li>Experienced with PVC, Polyethylene, Ductile Iron, GRP and Mild Steel</li>
      <li>Butt welding of PE pipelines</li>
    </ul>
    <ul class="bullets" style="left:280px;top:67px;width:170px">
      <li>Domestic water services</li>
      <li>Meter assemblies</li>
      <li>Relocation of existing water assets</li>
      <li>Dedicated commissioning crew for Swabbing, Hydrostatic Testing, Chlorinating and Water Quality Testing</li>
      <li>Complex live connections</li>
    </ul>

    <!-- Gas -->
    <svg class="service-icon" style="left:39px;top:163px" width="41" height="41" viewBox="0 0 41 41" fill="none" stroke="var(--navy)" stroke-width="1.2" aria-hidden="true">
      <circle cx="20.5" cy="20.5" r="19.5"/>
      <path d="M6 10h29M8 10v25M33 10v25"/>
      <rect x="12" y="13" width="17" height="21" rx="2"/>
      <rect x="16" y="17" width="7" height="12" rx="1"/>
      <path d="M18 20h3M23 22h3v5"/>
    </svg>
    <h3 class="sub-title" style="left:96px;top:160px">GAS INFRASTRUCTURE</h3>
    <ul class="bullets" style="left:96px;top:176px;width:340px">
      <li>Accredited contractor that can work on major Gas Authorities networks</li>
      <li>Constructability design reviews from highly experienced professionals</li>
      <li>Reticulation mains in single or common trench and larger pipelines</li>
      <li>Butt welding and electro-fusion</li>
      <li>Pre-laid gas services</li>
      <li>Pressure testing</li>
      <li>Complex gas tie-ins</li>
    </ul>

    <!-- Civil -->
    <svg class="service-icon" style="left:40px;top:259px" width="40" height="42" viewBox="0 0 40 42" fill="none" stroke="var(--navy)" stroke-width="1.2" aria-hidden="true">
      <path d="M6 20a14 14 0 0 1 28 0M16 6h8v8h-8zM3 20h34v4H3z"/>
      <path d="M8 24l-2 4 3 3-1 4 4 1 2 4 4-2 2 3 2-3 4 2 2-4 4-1-1-4 3-3-2-4"/>
      <circle cx="20" cy="31" r="4"/>
    </svg>
    <h3 class="sub-title" style="left:96px;top:259px">CIVIL CONSTRUCTION</h3>
    <ul class="bullets" style="left:96px;top:273px;width:340px">
      <li>Bulk earthworks</li>
      <li>Rehabilitation works</li>
      <li>Detailed excavations</li>
      <li>Hydro Excavation and underground service locating</li>
      <li>Landscaping</li>
      <li>General Civil works</li>
    </ul>

    <!-- Why choose us -->
    <div class="heading-row" style="top:351px"><span class="square"></span><h2 class="section-title">WHY CHOOSE US ?</h2></div>
    <div class="cream-panel" style="left:0;top:380px;width:96px;height:183px"></div>

    <div class="reason-icon" style="top:386px"><svg width="22" height="22" viewBox="0 0 22 22" fill="none" stroke="var(--navy)" stroke-width="1.1" aria-hidden="true"><circle cx="11" cy="7" r="5"/><path d="M8.8 7l1.6 1.6 3-3M2 10v6l4 4M20 10v6l-4 4M5 14l3 3M17 14l-3 3"/></svg></div>
    <div class="reason" style="top:381px">
      <h3 class="sub-title">QUALITY ASSURANCE</h3>
      <p>We appreciate the nuances of each individual project, while ensuring all relevant processes and procedures are understood and followed. This is critical to the success of any project and the longevity of the assets being installed.</p>
    </div>

    <div class="reason-icon" style="top:431px"><svg width="22" height="22" viewBox="0 0 22 22" fill="none" stroke="var(--navy)" stroke-width="1.1" aria-hidden="true"><circle cx="11" cy="5" r="3.5"/><path d="M9.5 5l1 1 2-2M1 11l4-2 4 2 3-1 4 1 5-2M3 13l5 5 2-1 3 2 6-6M9 12l4 4"/></svg></div>
    <div class="reason" style="top:435px">
      <h3 class="sub-title">TRUSTED PROFESSIONALS</h3>
      <p>With a team of project professionals and field staff with countless years of experience, you can rest assured that you are engaging a knowledgeable team that will deliver results.</p>
    </div>

    <div class="reason-icon" style="top:476px"><svg width="22" height="22" viewBox="0 0 22 22" fill="none" stroke="var(--navy)" stroke-width="1.1" aria-hidden="true"><circle cx="11" cy="11" r="10"/><circle cx="11" cy="11" r="7"/><path d="M11 6l4 1.5v3c0 3-2 4.5-4 5.5-2-1-4-2.5-4-5.5v-3z"/><path d="M9 11l1.5 1.5 2.5-3"/></svg></div>
    <div class="reason" style="top:479px">
      <h3 class="sub-title">SAFETY FOCUSED</h3>
      <p>We prioritise the safety of our people and others above all else. It’s not just talk, it is an engrained philosophy within our business.</p>
    </div>

    <div class="reason-icon" style="top:521px"><svg width="22" height="22" viewBox="0 0 22 22" fill="none" stroke="var(--navy)" stroke-width="1.1" aria-hidden="true"><circle cx="7" cy="6" r="3"/><path d="M2 20v-6a5 5 0 0 1 10 0v6M12 12h8v7h-8M17 3v2M14.5 6.5a2.5 2.5 0 1 1 5 0c0 1-1 1.5-1 2.5h-3c0-1-1-1.5-1-2.5z"/></svg></div>
    <div class="reason" style="top:523px">
      <h3 class="sub-title">COLLABORATIVE PROBLEM SOLVERS</h3>
      <p>We believe we have the right team in place to be ‘problem solvers’ for our clients and are focused on delivering whatever services are required to make their lives easier.</p>
    </div>

    <!-- Contact -->
    <div class="heading-row" style="top:581px;left:81px"><span class="square"></span><h2 class="section-title">CONTACT US</h2></div>

    <div class="contact-line" style="top:603px">
      <svg width="13" height="13" viewBox="0 0 13 13" fill="none" stroke="var(--navy)" stroke-width="0.9" aria-hidden="true"><circle cx="6.5" cy="6.5" r="6"/><path d="M6.5 10s-2.5-2.6-2.5-4.3a2.5 2.5 0 0 1 5 0c0 1.7-2.5 4.3-2.5 4.3z"/><circle cx="6.5" cy="5.7" r="0.9"/></svg>
      <span>4/18 Carrington Way, Westbrook VIC 3030</span>
    </div>
    <div class="contact-line" style="top:622px">
      <svg width="13" height="13" viewBox="0 0 13 13" fill="none" stroke="var(--navy)" stroke-width="0.9" aria-hidden="true"><circle cx="6.5" cy="6.5" r="6"/><path d="M4.3 3.6l1.2 1.5-.7 1c.5 1 1.1 1.6 2.1 2.1l1-.7 1.5 1.2-.8 1.1c-2.4-.4-4.3-2.3-4.7-4.7z"/></svg>
      <span>Michael Ross <b>0400 512 738</b> &nbsp;|&nbsp; Daniel Harper <b>0400 618 294</b></span>
    </div>
    <div class="contact-line" style="top:640px">
      <svg width="13" height="13" viewBox="0 0 13 13" fill="none" stroke="var(--navy)" stroke-width="0.9" aria-hidden="true"><circle cx="6.5" cy="6.5" r="6"/><rect x="3.5" y="4.5" width="6" height="4.2" rx="0.5"/><path d="M3.6 4.8l2.9 2.2 2.9-2.2"/></svg>
      <span>tenders@twgroundworks.com.au</span>
    </div>

    <div class="brand brand--back"><span class="brand__mark"></span>TW Groundworks</div>

    <footer class="footer footer--yellow">WWW.TWGROUNDWORKS.COM.AU</footer>
  </section>

</div>
</body>
</html>
```